Business card design for strategy and management consulting company. Would like to have a clean and professional business card, based on the attached logo. The company is a strategy and management consulting company focusing on sustainable business modlels based on economic, social and environmental market opportunities. Preferably the logo should be included on both sides of the design.

Industry/Entity Type

Business

Contact Information for Business Card

Håvard Lilleby, CEO/Management consultant
havard.lilleby@quarvenpartners.example
Mob: +47 948 26 317
Office: Vikfjell gate 14, pb 312 sentrum, N-0172 Oslo Norway

Requirements
Must have
• Include attached logo
Nice to have
• Would like to have the logo on both sides
Should not have
• Many colours.

```html
<!DOCTYPE html>
<html lang="en">
<head>
<meta charset="utf-8">
<title>Quarven business card</title>
<link rel="stylesheet" href="https://fonts.googleapis.com/css2?family=Roboto:wght@400;500;700&display=swap">
<style>
  :root {
    --ink: #1c1d1f;
    --paper: #ffffff;
    --accent: #f7d117;
    --text: #3a3a3a;
    --muted: #cfcfcf;
    --stage: #e6e6e4;
  }
  * { margin: 0; padding: 0; box-sizing: border-box; }
  html, body { width: 1200px; height: 911px; overflow: hidden; }
  body {
    background: var(--stage);
    font-family: "Roboto", Arial, sans-serif;
    display: flex;
    flex-direction: column;
    align-items: center;
    justify-content: center;
    gap: 50px;
  }
  .card {
    width: 700px;
    height: 400px;
    position: relative;
    overflow: hidden;
    box-shadow: 0 6px 18px rgba(0,0,0,0.18);
  }

  /* Front */
  .card-front { display: flex; background: var(--paper); }
  .front-info {
    width: 56%;
    padding: 48px 40px 44px 46px;
    display: flex;
    flex-direction: column;
    justify-content: space-between;
  }
  .person-name {
    color: var(--accent);
    font-weight: 500;
    font-size: 27px;
    letter-spacing: 0.5px;
    text-transform: uppercase;
    line-height: 1.1;
  }
  .person-title {
    color: var(--text);
    font-size: 17px;
    font-weight: 400;
    text-transform: uppercase;
    line-height: 1.25;
    margin-top: 4px;
  }
  .contact-list { list-style: none; color: var(--text); font-size: 14.5px; line-height: 1.5; }
  .contact-address { margin-bottom: 10px; }
  .contact-item { display: flex; align-items: center; gap: 10px; }
  .contact-icon { width: 15px; height: 15px; flex: none; }
  .front-brand {
    width: 44%;
    background: var(--ink);
    position: relative;
    display: flex;
    align-items: center;
    justify-content: center;
  }
  .front-brand::after {
    content: "";
    position: absolute;
    top: 0; right: 0; bottom: 0;
    width: 12px;
    background: var(--accent);
  }

  /* Wordmark */
  .wordmark {
    display: flex;
    align-items: center;
    gap: 10px;
    color: var(--paper);
    font-weight: 700;
    letter-spacing: -1px;
  }
  .wordmark-dot {
    width: 12px; height: 12px;
    border-radius: 50%;
    background: var(--accent);
  }
  .front-brand .wordmark { font-size: 62px; margin-right: 12px; }

  /* Back */
  .card-back {
    background: var(--ink);
    display: flex;
    flex-direction: column;
    align-items: center;
    justify-content: center;
  }
  .card-back .wordmark { font-size: 96px; }
  .card-back .wordmark-dot { width: 16px; height: 16px; }
  .back-web {
    position: absolute;
    bottom: 52px;
    left: 0; right: 0;
    text-align: center;
    color: var(--muted);
    font-size: 14px;
    letter-spacing: 6px;
  }
</style>
</head>
<body>

<section class="card card-front" aria-label="Business card front">
  <div class="front-info">
    <header>
      <h1 class="person-name">Håvard Lilleby</h1>
      <p class="person-title">CEO/Management<br>Consultant</p>
    </header>
    <ul class="contact-list">
      <li class="contact-address">Vikfjell gate 14,<br>pb 312 sentrum, N-0172 Oslo Norway</li>
      <li class="contact-item">
        <svg class="contact-icon" viewBox="0 0 16 16" aria-hidden="true"><rect x="4" y="1" width="8" height="14" rx="1.5" fill="none" stroke="#f7d117" stroke-width="1.6"/><circle cx="8" cy="12.3" r="0.9" fill="#f7d117"/></svg>
        +47 948 26 317
      </li>
      <li class="contact-item">
        <svg class="contact-icon" viewBox="0 0 16 16" aria-hidden="true"><rect x="1" y="3" width="14" height="10" rx="1" fill="#f7d117"/><path d="M1.5 3.8 8 9l6.5-5.2" fill="none" stroke="#fff" stroke-width="1.3"/></svg>
        havard.lilleby@quarvenpartners.example
      </li>
      <li class="contact-item">
        <svg class="contact-icon" viewBox="0 0 16 16" aria-hidden="true"><circle cx="8" cy="8" r="7" fill="#f7d117"/><path d="M1 8h14M8 1c-3 3.5-3 10.5 0 14M8 1c3 3.5 3 10.5 0 14" fill="none" stroke="#fff" stroke-width="1"/></svg>
        www.quarvenpartners.example
      </li>
    </ul>
  </div>
  <div class="front-brand">
    <div class="wordmark"><span class="wordmark-dot"></span>Quarven</div>
  </div>
</section>

<section class="card card-back" aria-label="Business card back">
  <div class="wordmark"><span class="wordmark-dot"></span>Quarven</div>
  <p class="back-web">www.quarvenpartners.example</p>
</section>

</body>
</html>
```